Business card design for immigration consulting business

We need business card design for a company called T&R Migration Advisors Inc. This is a boutique immigration consulting and foreign recruitment agency owned and managed by two partners.
The business card will be used by partners \ owners of the business. The best way to describe the business would be committed to client, passionate about providing top-notch services, engaging, competent, professional

Target Market(s)

We work with individuals in and outside of Canada who need immigration advise as well as Canadian businesses looking to hire or sponsor foreign workers to Canada

Industry/Entity Type

Consulting

Contact Information for Business Card

The business card should have a standard size and horizontal lay-out

Font styles to use
Serif

Colors
f04a50
ec1f27
cbcbcb
dbdbdb

Requirements
Must have
• The business card mush have our logo, name of the company first and last name of the partner, position, phone, cell, fax, e-mail, skype, web-site
• Our first choice would a classic design with minimalist looks and elegant fonts and colors, but we are open minded to any creative ideas too
Nice to have
• On the other side it may have the description of the company: Immigration and Foreign Recruitment Services
• We're considering using stamping \ lettering on our business cards
• It would be nice if the business card would have white space, in case someone would like to make notes on it.
• One (back side) side of the business card can be all red with white logo
Should not have
• We do not want to have our pictures on the business card
• We do no want to have Canadian maple leaf on the business card as we already have one in our logo

```html
<!DOCTYPE html>
<html lang="en">
<head>
<meta charset="utf-8">
<title>T&amp;R Migration Advisors Inc. – Business Card</title>
<link href="https://fonts.googleapis.com/css2?family=Tinos:wght@400;700&family=Source+Sans+3:wght@400;600&display=swap" rel="stylesheet">
<style>
  :root {
    --stage: #a3a3a3;
    --card-light: #ffffff;
    --card-dark: #6d6d6d;
    --ink-grey: #666666;
    --ink-dark: #333333;
    --accent-red: #ec1f27;
    --rule: #8a8a8a;
    --white: #ffffff;
  }
  * { margin: 0; padding: 0; box-sizing: border-box; }
  html, body { width: 1200px; height: 900px; overflow: hidden; }
  body {
    background: var(--stage);
    position: relative;
    font-family: "Source Sans 3", "Helvetica Neue", Arial, sans-serif;
  }
  .card {
    position: absolute;
    top: 301px;
    width: 520px;
    height: 297px;
  }
  .card--front { left: 65px; background: var(--card-light); }
  .card--back  { left: 615px; background: var(--card-dark); }

  .wordmark {
    display: flex;
    align-items: center;
    justify-content: center;
    gap: 10px;
    font-family: "Tinos", "Times New Roman", serif;
    font-weight: 400;
    white-space: nowrap;
  }
  .wordmark__dot {
    border-radius: 50%;
    background: var(--accent-red);
    flex: none;
  }

  /* Front: brand left, contact details right */
  .card--front .brand-panel {
    position: absolute;
    left: 0; top: 0;
    width: 260px; height: 100%;
    display: flex;
    align-items: center;
    justify-content: center;
  }
  .card--front .wordmark { font-size: 30px; color: var(--ink-grey); }
  .card--front .wordmark__dot { width: 12px; height: 12px; }
  .divider {
    position: absolute;
    left: 260px; top: 50px;
    width: 1px; height: 197px;
    background: var(--rule);
  }
  .details {
    position: absolute;
    left: 290px; top: 0;
    width: 210px; height: 100%;
    display: flex;
    flex-direction: column;
    justify-content: center;
  }
  .person__name {
    font-family: "Tinos", "Times New Roman", serif;
    font-size: 20px;
    letter-spacing: 0.5px;
    color: var(--accent-red);
    line-height: 24px;
  }
  .person__role {
    font-size: 15px;
    color: var(--ink-dark);
    line-height: 20px;
  }
  .person__rule {
    width: 146px;
    height: 1px;
    background: var(--rule);
    margin: 10px 0 10px;
  }
  .contact {
    list-style: none;
    font-size: 14.5px;
    line-height: 20.5px;
    color: var(--ink-dark);
    white-space: nowrap;
  }
  .contact__label { color: var(--accent-red); font-weight: 600; }

  /* Back */
  .card--back .wordmark {
    position: absolute;
    left: 0; right: 0; top: 105px;
    font-size: 44px; color: var(--white);
  }
  .card--back .wordmark__dot { width: 16px; height: 16px; }
  .website {
    position: absolute;
    bottom: 28px;
    left: 0; right: 0;
    text-align: center;
    font-family: "Tinos", "Times New Roman", serif;
    font-weight: 700;
    font-size: 20px;
    letter-spacing: 1.5px;
    color: var(--white);
  }
</style>
</head>
<body>
  <section class="card card--front" aria-label="Card front">
    <div class="brand-panel">
      <div class="wordmark"><span class="wordmark__dot"></span>T&amp;R Migration</div>
    </div>
    <div class="divider"></div>
    <div class="details">
      <p class="person__name">DANIEL REYES</p>
      <p class="person__role">Managing Director</p>
      <div class="person__rule"></div>
      <ul class="contact">
        <li><span class="contact__label">P:</span> (044)987654321</li>
        <li><span class="contact__label">M:</span> (044)987654321</li>
        <li><span class="contact__label">F:</span> (044)987654321</li>
        <li><span class="contact__label">E:</span> info@trmigration.com</li>
        <li><span class="contact__label">S:</span> trmigration.reyes</li>
      </ul>
    </div>
  </section>

  <section class="card card--back" aria-label="Card back">
    <div class="wordmark"><span class="wordmark__dot"></span>T&amp;R Migration</div>
    <p class="website">www.trmigration.com</p>
  </section>
</body>
</html>
```